High end boutique food product label

We are looking for a label design to be used on our range of high end food products. We don't have a design or colour scheme in mind and are interested to see what ideas are submitted.
We would like it to feel sophisticated, chic, and eye-catching.
All of our products are handmade in Australia using Australian ingredients.
The graphics for the label will need to be scaleable to be fit a variety of labels from small squat jars with labels sized 3.5cm high and 7cm wide, to tall thin bottles with labels that are 14cm high and 4.5cm wide.
We would be interested in working with the winning designer to create these different sized labels.
The label submitted for this project should be 14cm high and 4.5cm wide, it should include our logo (file supplied in .jpeg and .ai), the product name 'Extra Virgin Olive Oil' and the size '250ml'.
This is just the front label on a bottle, we are not expecting a rear label to be created currently.
You are welcome to use any fonts you think will look good but the fonts used in our logo are Allaina Medium and Bebas Kai Regular.

```html
<!DOCTYPE html>
<html lang="en">
<head>
<meta charset="utf-8">
<title>R&amp;K Pantry – Extra Virgin Olive Oil Label</title>
<link rel="stylesheet" href="https://fonts.googleapis.com/css2?family=Montserrat:wght@700;800&display=swap">
<style>
  :root {
    --label-yellow: #FBDB8C;
    --leaf-tint: #EFCB7E;
    --brown: #3D2817;
    --cream: #F6E7C8;
    --page: #FFFFFF;
  }
  * { margin: 0; padding: 0; box-sizing: border-box; }
  html, body {
    width: 1200px; height: 1200px; overflow: hidden;
    background: var(--page);
  }
  .canvas { position: relative; width: 1200px; height: 1200px; }
  .label {
    position: absolute; left: 420px; top: 40px;
    width: 359px; height: 1120px;
    background: var(--label-yellow);
    overflow: hidden;
    font-family: "Montserrat", Arial, sans-serif;
    color: var(--brown);
  }
  .label__pattern {
    position: absolute; inset: 0;
    background:
      radial-gradient(ellipse 120px 160px at 40px 80px, var(--leaf-tint) 0%, transparent 70%),
      radial-gradient(ellipse 110px 150px at 320px 230px, var(--leaf-tint) 0%, transparent 70%),
      radial-gradient(ellipse 120px 150px at 60px 460px, var(--leaf-tint) 0%, transparent 70%),
      radial-gradient(ellipse 100px 130px at 80px 870px, var(--leaf-tint) 0%, transparent 70%),
      radial-gradient(ellipse 150px 190px at 280px 980px, var(--leaf-tint) 0%, transparent 70%);
    opacity: 0.9;
  }
  .label__frame {
    position: absolute; left: 13px; top: 13px; right: 13px; bottom: 13px;
    border: 3.3px solid var(--brown);
  }
  .brand-badge {
    position: absolute; left: 122px; top: 62px;
    width: 114px; height: 114px; border-radius: 50%;
    background: var(--brown);
    display: flex; flex-direction: column; align-items: center; justify-content: center;
    color: var(--cream); font-weight: 700; text-align: center; line-height: 1.1;
  }
  .brand-badge__initials { font-size: 24px; }
  .brand-badge__name { font-size: 11px; letter-spacing: 0.1em; text-transform: uppercase; }
  .divider {
    position: absolute; left: 45px; width: 269px; height: 2px;
  }
  .divider--top { top: 380px; }
  .divider--bottom { top: 1038px; }
  .product__kind {
    position: absolute; left: 0; right: 0; top: 477px;
    text-align: center; font-size: 15px; font-weight: 700;
    letter-spacing: 0.28em; padding-left: 0.28em;
  }
  .product__name {
    position: absolute; left: 0; right: 0; text-align: center;
    font-size: 78px; font-weight: 800; line-height: 1; letter-spacing: -0.01em;
  }
  .product__name--first { top: 503px; }
  .product__name--second { top: 604px; }
  .product__size {
    position: absolute; left: 0; right: 0; top: 1053px;
    text-align: center; font-size: 14px; font-weight: 700; letter-spacing: 0.12em;
  }
</style>
</head>
<body>
<main class="canvas">
  <section class="label">
    <div class="label__pattern" role="img" aria-label="Faint olive branch and leaf pattern"></div>
    <div class="label__frame"></div>

    <div class="brand-badge">
      <span class="brand-badge__initials">R&amp;K</span>
      <span class="brand-badge__name">Pantry</span>
    </div>

    <svg class="divider divider--top" viewBox="0 0 269 2" aria-hidden="true">
      <circle cx="1" cy="1" r="1" fill="#3D2817"/>
      <line x1="10" y1="1" x2="259" y2="1" stroke="#3D2817" stroke-width="1.6"/>
      <circle cx="268" cy="1" r="1" fill="#3D2817"/>
    </svg>

    <p class="product__kind">EXTRA VIRGIN</p>
    <h1 class="product__name product__name--first">OLIVE</h1>
    <h1 class="product__name product__name--second">OIL</h1>

    <svg class="divider divider--bottom" viewBox="0 0 269 2" aria-hidden="true">
      <circle cx="1" cy="1" r="1" fill="#3D2817"/>
      <line x1="10" y1="1" x2="259" y2="1" stroke="#3D2817" stroke-width="1.6"/>
      <circle cx="268" cy="1" r="1" fill="#3D2817"/>
    </svg>

    <p class="product__size">250 ML</p>
  </section>
</main>
</body>
</html>
```